Spiral Bound Classy Marketing Planner Cover Design

A5 marketing planner book cover requiredClassy, minimalist design for female entrepreneurs. The inside is all in grey and is a minimalist uncluttered design. Name of the planner is It's Time Marketing Recipe PlannerHeader font inside the planner is Shelby and other font is Lato Brand colours are teal and grey.The printing format has changed and as such I am looking for a new cover design to make this marketing planner look classy and engaging. Would prefer my logo to be on the back. We have the option for a 10cm x 10cm foil detail to be added on the front cover, feel free to add this to your design.This is for a spiral bound book - A5 front cover and A5 back cover - no spine required.

Target Market(s)

Female entrepreneurs

Industry/Entity Type

Marketing

Colors
33b8a4
ffffff

Requirements
Must have
• Front and back designs
• A5
Should not have
• Large illustrations
• People in the design
• Spine design

```html
<!DOCTYPE html>
<html lang="en">
<head>
<meta charset="utf-8">
<title>Bold Hour Promo Blueprint Planner – Covers</title>
<link rel="stylesheet" href="https://fonts.googleapis.com/css2?family=Lato:wght@400;700;900&family=Yellowtail&display=swap">
<style>
  :root {
    --teal: #00a9bd;
    --white: #ffffff;
    --silver: #dcdcdc;
    --grey: #9d9d9f;
    --edge: #ececec;
    --page: #ffffff;
  }
  * { margin: 0; padding: 0; box-sizing: border-box; }
  html, body {
    width: 1173px;
    height: 1200px;
    overflow: hidden;
    background: var(--page);
  }
  .spread {
    position: relative;
    width: 1173px;
    height: 1200px;
  }
  .cover {
    position: absolute;
    top: 271px;
    width: 455px;
    height: 649px;
  }
  .cover--front {
    left: 93px;
    background: var(--teal);
  }
  .cover--back {
    left: 593px;
    background: var(--white);
    border: 1px solid var(--edge);
  }
  .cover__lines {
    position: absolute;
    inset: 0;
    width: 100%;
    height: 100%;
  }
  .cover__lines line {
    stroke: var(--white);
    stroke-width: 2;
    vector-effect: non-scaling-stroke;
  }
  .title-block {
    position: absolute;
    right: 33px;
    top: 270px;
    text-align: right;
  }
  .title-block__name {
    font-family: "Yellowtail", cursive;
    font-weight: 400;
    font-size: 56px;
    line-height: 1;
    color: var(--silver);
    letter-spacing: 1px;
    white-space: nowrap;
  }
  .title-block__sub {
    margin-top: 6px;
    font-family: "Lato", sans-serif;
    font-weight: 400;
    font-size: 13px;
    letter-spacing: 2.6px;
    color: var(--silver);
    text-transform: uppercase;
    white-space: nowrap;
  }
  .brand {
    position: absolute;
    left: 156px;
    top: 216px;
    display: flex;
    flex-direction: column;
    align-items: flex-start;
  }
  .brand__frame {
    width: 146px;
    height: 166px;
    border: 1.5px solid var(--grey);
    display: flex;
    align-items: center;
    justify-content: center;
    text-align: center;
  }
  .brand__name {
    font-family: "Lato", sans-serif;
    font-weight: 900;
    font-size: 24px;
    line-height: 1.1;
    color: var(--teal);
  }
  .brand__tagline {
    margin-top: 8px;
    font-family: "Lato", sans-serif;
    font-weight: 700;
    font-size: 8px;
    line-height: 1.4;
    letter-spacing: 1.3px;
    color: var(--grey);
    text-transform: uppercase;
    text-align: left;
    white-space: nowrap;
  }
</style>
</head>
<body>
  <main class="spread">
    <section class="cover cover--front" aria-label="Front cover">
      <svg class="cover__lines" viewBox="0 0 419 595" preserveAspectRatio="none" aria-hidden="true">
        <line x1="79" y1="0" x2="0" y2="145"/>
        <line x1="174" y1="0" x2="419" y2="132"/>
        <line x1="0" y1="467" x2="237" y2="595"/>
        <line x1="419" y1="407" x2="319" y2="595"/>
      </svg>
      <div class="title-block">
        <h1 class="title-block__name">Bold Hour</h1>
        <p class="title-block__sub">Promo Blueprint Planner</p>
      </div>
    </section>

    <section class="cover cover--back" aria-label="Back cover">
      <div class="brand">
        <div class="brand__frame">
          <span class="brand__name">Copper<br>Whisk<br>Studio</span>
        </div>
        <p class="brand__tagline">Promotion with the best<br>blend for steady growth</p>
      </div>
    </section>
  </main>
</body>
</html>
```